Acupuncture business needs business card design

I need a business card for an acupuncture clinic called "Summit Wellpath"
It will need the following details:
My name: Marcus Thelwick
Acupuncturist
Member KPTG
BVF Treatment Provider
Ph numbers: 482 1358 027 514 3820
Email: marcus@swpath.example.nz
On the back it will need a table with 2 columns for appointments, one column for time and one for date.

Industry/Entity Type

Clinic

Contact Information for Business Card

Marcus Thelwick
Acupuncturist
Member KPTG
BVF Treatment Provider
Email: marcus@swpath.example.nz

Requirements
Must have
• Marcus Thelwick
• Acupuncturist
• Member KPTG
• BVF Treatment Provider
• Ph numbers: 482 1358 027 514 3820
• Email: marcus@swpath.example.nz
• On the back it will need a table with 2 columns for appointments, one column for time and one for date.

```html
<!DOCTYPE html>
<html lang="en">
<head>
<meta charset="utf-8">
<title>Summit Wellpath – Business Card</title>
<link href="https://fonts.googleapis.com/css2?family=Open+Sans:wght@400;600;700&display=swap" rel="stylesheet">
<style>
  :root {
    --backdrop: #e6e8ea;
    --card-white: #ffffff;
    --brand-blue: #1ea9dc;
    --brand-deep: #1780ab;
    --teal: #17788f;
    --teal-faint: rgba(255,255,255,0.12);
    --slot: #d4e6ec;
    --ink: #333b40;
    --ink-soft: #5d666b;
  }
  * { box-sizing: border-box; margin: 0; padding: 0; }
  html, body { width: 1200px; height: 948px; overflow: hidden; }
  body {
    background: var(--backdrop);
    font-family: "Open Sans", Arial, sans-serif;
    display: flex;
    align-items: center;
    justify-content: center;
    gap: 40px;
  }
  .card {
    width: 540px;
    height: 309px;
    position: relative;
    overflow: hidden;
    box-shadow: 0 6px 18px rgba(0,0,0,0.18);
  }

  /* Front */
  .card-front { background: var(--card-white); color: var(--ink); }
  .brand {
    position: absolute; left: 34px; top: 26px;
    display: flex; align-items: center; gap: 12px;
  }
  .brand-dot {
    width: 34px; height: 34px; border-radius: 50%;
    background: var(--brand-blue);
  }
  .brand-name {
    font-size: 31px; font-weight: 700; color: var(--brand-blue);
    line-height: 1;
  }
  .brand-tagline {
    position: absolute; left: 81px; top: 66px;
    font-size: 10px; letter-spacing: 3.6px; color: var(--brand-blue);
    text-transform: uppercase;
  }
  .band-rule {
    position: absolute; left: 0; right: 0; height: 2px;
    background: var(--brand-deep);
  }
  .band-rule.top { top: 92px; }
  .band-rule.bottom { top: 163px; }
  .band {
    position: absolute; left: 0; right: 0; top: 98px; height: 59px;
    background: var(--brand-blue); color: #fff;
    padding: 9px 0 0 81px;
    font-size: 13px; line-height: 20px;
  }
  .band .name { font-weight: 700; }
  .contact {
    position: absolute; left: 81px; top: 180px;
    font-size: 14px; line-height: 26px; color: var(--ink);
  }
  .contact-line { display: flex; align-items: center; gap: 10px; }
  .contact-line svg { width: 14px; height: 14px; flex: none; }
  .address {
    position: absolute; left: 81px; bottom: 22px;
    font-size: 13px; line-height: 19px; color: var(--ink-soft);
  }

  /* Back */
  .card-back { background: var(--teal); color: #fff; }
  .back-emblem {
    position: absolute; left: 180px; top: 50px;
    width: 200px; height: 200px; border-radius: 50%;
    background: var(--teal-faint);
  }
  .appointments {
    position: absolute; left: 40px; top: 36px;
    display: grid; grid-template-columns: 190px 190px; column-gap: 24px; row-gap: 14px;
  }
  .appointments .col-head { font-size: 15px; letter-spacing: 0.5px; }
  .appointments .slot { height: 24px; background: var(--slot); opacity: 0.9; }
  .web {
    position: absolute; left: 40px; bottom: 30px;
    font-size: 16px; letter-spacing: 2px;
  }
</style>
</head>
<body>
  <section class="card card-front" aria-label="Business card front">
    <div class="brand">
      <span class="brand-dot"></span>
      <span class="brand-name">Summit Wellpath</span>
    </div>
    <div class="brand-tagline">Acupuncture Physiotherapy</div>

    <div class="band-rule top"></div>
    <div class="band">
      <div><span class="name">Marcus Thelwick,</span> Acupuncturist, Member KPTG</div>
      <div>BVF Treatment Provider</div>
    </div>
    <div class="band-rule bottom"></div>

    <div class="contact">
      <div class="contact-line">
        <svg viewBox="0 0 16 16" aria-hidden="true"><circle cx="8" cy="8" r="8" fill="#1ea9dc"/><path d="M5.3 4.2l1.4 1.6-.8 1c.6 1.2 1.5 2.1 2.7 2.7l1-.8 1.6 1.4-.9 1.3c-2.9-.6-5.2-2.9-5.8-5.8z" fill="#fff"/></svg>
        <span>482 1358 · 027 514 3820</span>
      </div>
      <div class="contact-line">
        <svg viewBox="0 0 16 16" aria-hidden="true"><circle cx="8" cy="8" r="8" fill="#1ea9dc"/><rect x="4" y="5" width="8" height="6" fill="#fff"/><path d="M4 5l4 3.2L12 5" fill="none" stroke="#1ea9dc" stroke-width="1"/></svg>
        <span>marcus@swpath.example.nz</span>
      </div>
    </div>

    <div class="address">
      <div>Street Name, City Name</div>
      <div>Zipcode-01234</div>
    </div>
  </section>

  <section class="card card-back" aria-label="Business card back">
    <div class="back-emblem"></div>
    <div class="appointments">
      <div class="col-head">Date</div>
      <div class="col-head">Time</div>
      <div class="slot"></div><div class="slot"></div>
      <div class="slot"></div><div class="slot"></div>
      <div class="slot"></div><div class="slot"></div>
    </div>
    <div class="web">www.swpath.example.nz</div>
  </section>
</body>
</html>
```